Resinora color chart design

We are in need to have a color chart (pdf to be displayed on our website-www.resinora-coat.example as well as for print) to show customers what their color choices are for our metallic epoxy pigments. We would like it to be modern amd clean. A white background will allow the color swatches to stand out. our company colors are orange, grey and white. Looking for the color swatches to be as large as possible while still being able to display our logo, contact info and disclaimers. We are open to any design ideas. If needed it can be put on two pages.

Additional info to add: Resinora Lustre Tint Powders are special effect pigments composed of mica nano-particles coated with various organic and inorganic pigments to create pearlescent and iridescent effects that mimic the
natural look of stone and rock formations. These unique pigments are designed to be field blended with Resinora Artisan Sheen clear epoxy. When the metallic particles are mixed with our epoxy they give the coating a shine that reflects light and creates an eye-catching dramatic color. For the most vivid color and dynamic effects we recommend (1) 16oz jar of metallic pigment for each 3 Gallon kit of our Artisan Sheen Epoxy.

Disclaimer: The colors on this chart are represented as closely as possible. Variations should be expected due to differences in substrate conditions, thickness of application, speed of curing, blending of colors, application technique, color of initial primer coat and screen resolution. For additional information and application instructions visit www.resinora-coat.example

Contact info: Tel. 1-888-555-0174
www.resinora-coat.example

Target Market(s)

Online. This will be a link on our website

Font styles to use
Sans Serif

Colors
f37122
5c5c5c
ffffff

Requirements
Must have
• A white background will allow the color swatches to stand out. Disclaimer should be in small print but still readable.
Nice to have
• Can use our company colors as part of the design
Should not have
• Should not look and feel cluttered.

```html
<!DOCTYPE html>
<html lang="en">
<head>
<meta charset="utf-8">
<title>Resinora Metallic Pigment Colour Chart</title>
<link rel="stylesheet" href="https://fonts.googleapis.com/css2?family=Questrial&family=Montserrat:wght@600;700&display=swap">
<style>
  :root {
    --brand-orange: #f37122;
    --brand-grey: #5c5c5c;
    --ring-grey: #8a8a8a;
    --paper: #ffffff;
    --ink: #2b2b2b;
    --backdrop: #3b3b3b;
  }
  * { box-sizing: border-box; margin: 0; padding: 0; }
  html, body { width: 1200px; height: 1200px; overflow: hidden; }
  body { background: var(--backdrop); position: relative; font-family: "Questrial", sans-serif; color: var(--ink); }

  .sheet {
    position: absolute; top: 253px; width: 522px; height: 733px;
    background: var(--paper); overflow: hidden;
    box-shadow: 0 6px 18px rgba(0,0,0,.45);
  }
  .sheet--front { left: 52px; }
  .sheet--back { left: 624px; }

  .brand { position: absolute; display: flex; align-items: center; }
  .brand__dot { border-radius: 50%; background: var(--brand-orange); flex: none; }
  .brand__text { display: flex; flex-direction: column; }
  .brand__name { font-family: "Questrial", sans-serif; color: var(--brand-orange); line-height: 1; }
  .brand__tagline { color: var(--brand-grey); }

  .brand--front { left: 103px; top: 34px; gap: 25px; }
  .brand--front .brand__dot { width: 74px; height: 74px; }
  .brand--front .brand__name { font-size: 44px; }
  .brand--front .brand__tagline { font-size: 12px; margin-top: 6px; }

  .brand--back { left: 153px; top: 597px; gap: 17px; transform: translateY(-50%); }
  .brand--back .brand__dot { width: 50px; height: 50px; }
  .brand--back .brand__name { font-size: 28px; }
  .brand--back .brand__tagline { font-size: 8px; margin-top: 3px; }

  .intro {
    position: absolute; left: 26px; top: 132px; width: 471px;
    font-size: 8.3px; line-height: 1.27; text-align: justify; color: #3a3a3a;
  }
  .intro strong { font-weight: 700; }
  .intro .intro__last { display: block; text-align: center; }

  .swatch {
    position: absolute; left: calc(var(--x) - 53px); top: calc(var(--y) - 53px);
    width: 106px; height: 106px; border-radius: 50%;
    border: 4px solid var(--ring-grey); padding: 5px;
    background: radial-gradient(circle at 35% 30%, rgba(255,255,255,.22), rgba(255,255,255,0) 60%), var(--c);
    background-clip: content-box;
  }
  .swatch--orange { border-color: var(--brand-orange); }

  .swatch-name {
    position: absolute; left: var(--x); top: var(--y); transform: translateX(-50%);
    font-family: "Montserrat", sans-serif; font-weight: 600; font-size: 12px;
    letter-spacing: .2px; color: #1e1e1e; white-space: nowrap;
  }

  .disclaimer {
    position: absolute; left: 32px; top: 628px; width: 466px;
    font-size: 6.4px; line-height: 1.3; color: #444;
  }
  .disclaimer strong { font-weight: 700; }

  .footer { position: absolute; left: 0; bottom: 0; width: 522px; height: 34px; }
  .footer__band { position: absolute; left: 0; top: 0; }
  .footer__contact {
    position: absolute; left: 30px; top: 0; height: 34px; display: flex; align-items: center; gap: 20px;
    color: var(--paper); font-family: "Montserrat", sans-serif; font-weight: 600; font-size: 11.5px;
  }
  .footer__item { display: flex; align-items: center; gap: 7px; white-space: nowrap; }
  .footer__icon { flex: none; display: block; }
</style>
</head>
<body>

<section class="sheet sheet--front" aria-label="Colour chart, front">
  <div class="brand brand--front">
    <span class="brand__dot"></span>
    <div class="brand__text">
      <span class="brand__name">resinora</span>
      <span class="brand__tagline">Floor finishes built to shine.</span>
    </div>
  </div>

  <p class="intro"><strong>Resinora</strong> Lustre Tint Powders are special effect pigments composed of mica nano-particles coated with various organic and inorganic pigments to create pearlescent and iridescent effects that mimic the natural look of stone and rock formations. These unique pigments are designed to be field blended with Resinora Artisan Sheen clear epoxy. When the metallic particles are mixed with our epoxy they give the coating a shine that reflects light and creates an eye-catching dramatic color. For the most vivid color and dynamic effects we recommend <span class="intro__last">(1) 16oz jar of metallic pigment for each 3 Gallon kit of our Artisan Sheen Epoxy.</span></p>

  <div class="swatch" style="--x:72px;--y:281px;--c:#f7b500"></div>
  <div class="swatch swatch--orange" style="--x:204px;--y:281px;--c:#d9921c"></div>
  <div class="swatch" style="--x:330px;--y:281px;--c:#c8680a"></div>
  <div class="swatch swatch--orange" style="--x:454px;--y:283px;--c:#b65a12"></div>
  <span class="swatch-name" style="--x:75px;--y:345px">CANARY</span>
  <span class="swatch-name" style="--x:207px;--y:345px">CAIRO</span>
  <span class="swatch-name" style="--x:330px;--y:345px">ORANGE GOLD</span>
  <span class="swatch-name" style="--x:452px;--y:347px">BRASS</span>

  <div class="swatch" style="--x:72px;--y:431px;--c:#0d9a7c"></div>
  <div class="swatch swatch--orange" style="--x:204px;--y:431px;--c:#1b4c38"></div>
  <div class="swatch" style="--x:330px;--y:431px;--c:#263f2a"></div>
  <div class="swatch swatch--orange" style="--x:454px;--y:431px;--c:#b03a0a"></div>
  <span class="swatch-name" style="--x:76px;--y:494px">SEA GREEN</span>
  <span class="swatch-name" style="--x:210px;--y:494px">FOREST GREEN</span>
  <span class="swatch-name" style="--x:331px;--y:495px">GREEN APPLE</span>
  <span class="swatch-name" style="--x:451px;--y:495px">COPPER</span>

  <div class="swatch" style="--x:72px;--y:581px;--c:#6e0d0d"></div>
  <div class="swatch swatch--orange" style="--x:204px;--y:581px;--c:#7b2708"></div>
  <div class="swatch" style="--x:330px;--y:581px;--c:#6e3214"></div>
  <div class="swatch swatch--orange" style="--x:454px;--y:581px;--c:#2e1a10"></div>
  <span class="swatch-name" style="--x:67px;--y:647px">WINE RED</span>
  <span class="swatch-name" style="--x:203px;--y:647px">CINNAMON</span>
  <span class="swatch-name" style="--x:328px;--y:647px">PENNY</span>
  <span class="swatch-name" style="--x:450px;--y:647px">COFFEE</span>

  <footer class="footer">
    <svg class="footer__band" width="522" height="34" viewBox="0 0 522 34" aria-hidden="true">
      <rect x="330" y="19" width="192" height="15" fill="var(--brand-grey)"/>
      <path d="M0 0 H320 C338 0 342 20 346 34 H0 Z" fill="var(--brand-orange)"/>
    </svg>
    <div class="footer__contact">
      <span class="footer__item">
        <svg class="footer__icon" width="11" height="11" viewBox="0 0 24 24" aria-hidden="true"><path fill="#fff" d="M6.6 10.8a15.1 15.1 0 0 0 6.6 6.6l2.2-2.2a1 1 0 0 1 1-.25 11.4 11.4 0 0 0 3.6.57 1 1 0 0 1 1 1V20a1 1 0 0 1-1 1A17 17 0 0 1 3 4a1 1 0 0 1 1-1h3.5a1 1 0 0 1 1 1c0 1.25.2 2.45.57 3.57a1 1 0 0 1-.25 1z"/></svg>
        1-888-555-0174
      </span>
      <span class="footer__item">
        <svg class="footer__icon" width="11" height="11" viewBox="0 0 24 24" aria-hidden="true"><circle cx="12" cy="12" r="10" fill="none" stroke="#fff" stroke-width="2.2"/><path d="M2 12h20M12 2c3 3 3 17 0 20M12 2c-3 3-3 17 0 20" fill="none" stroke="#fff" stroke-width="1.8"/></svg>
        www.resinora-coat.example
      </span>
    </div>
  </footer>
</section>

<section class="sheet sheet--back" aria-label="Colour chart, back">
  <div class="swatch" style="--x:70px;--y:91px;--c:#6e3f93"></div>
  <div class="swatch swatch--orange" style="--x:197px;--y:91px;--c:#24085f"></div>
  <div class="swatch" style="--x:326px;--y:91px;--c:#111111"></div>
  <div class="swatch swatch--orange" style="--x:452px;--y:91px;--c:#b3053e"></div>
  <span class="swatch-name" style="--x:66px;--y:158px">LILAC</span>
  <span class="swatch-name" style="--x:195px;--y:158px">GRAPE</span>
  <span class="swatch-name" style="--x:328px;--y:158px">GUNMETAL</span>
  <span class="swatch-name" style="--x:457px;--y:158px">BUBBLEGUM</span>

  <div class="swatch" style="--x:70px;--y:250px;--c:#0a6f8c"></div>
  <div class="swatch swatch--orange" style="--x:201px;--y:250px;--c:#0a4aa3"></div>
  <div class="swatch" style="--x:326px;--y:250px;--c:#938100"></div>
  <div class="swatch swatch--orange" style="--x:452px;--y:250px;--c:#f25e0c"></div>
  <span class="swatch-name" style="--x:67px;--y:318px">SKY BLUE</span>
  <span class="swatch-name" style="--x:202px;--y:318px">OCEAN BLUE</span>
  <span class="swatch-name" style="--x:333px;--y:318px">OLIVE YELLOW</span>
  <span class="swatch-name" style="--x:457px;--y:318px">TANGERINE</span>

  <div class="swatch" style="--x:70px;--y:413px;--c:#ecdfd8"></div>
  <div class="swatch swatch--orange" style="--x:201px;--y:413px;--c:#c4c4c4"></div>
  <div class="swatch" style="--x:326px;--y:413px;--c:#6d6464"></div>
  <div class="swatch swatch--orange" style="--x:452px;--y:413px;--c:#3e393a"></div>
  <span class="swatch-name" style="--x:67px;--y:476px">PEARL</span>
  <span class="swatch-name" style="--x:200px;--y:476px">DIAMOND</span>
  <span class="swatch-name" style="--x:331px;--y:476px">SILVER</span>
  <span class="swatch-name" style="--x:454px;--y:476px">TITANIUM</span>

  <div class="brand brand--back">
    <span class="brand__dot"></span>
    <div class="brand__text">
      <span class="brand__name">resinora</span>
      <span class="brand__tagline">Floor finishes built to shine.</span>
    </div>
  </div>

  <p class="disclaimer"><strong>Disclaimer:</strong> The colors on this chart are represented as closely as possible. Variations should be expected due to differences in substrate conditions, thickness of application, speed of curing, blending of colors, application technique, color of initial primer coat and screen resolution. For additional information and application instructions visit www.resinora-coat.example</p>

  <footer class="footer">
    <svg class="footer__band" width="522" height="34" viewBox="0 0 522 34" aria-hidden="true">
      <rect x="330" y="19" width="192" height="15" fill="var(--brand-grey)"/>
      <path d="M0 0 H320 C338 0 342 20 346 34 H0 Z" fill="var(--brand-orange)"/>
    </svg>
    <div class="footer__contact">
      <span class="footer__item">
        <svg class="footer__icon" width="11" height="11" viewBox="0 0 24 24" aria-hidden="true"><path fill="#fff" d="M6.6 10.8a15.1 15.1 0 0 0 6.6 6.6l2.2-2.2a1 1 0 0 1 1-.25 11.4 11.4 0 0 0 3.6.57 1 1 0 0 1 1 1V20a1 1 0 0 1-1 1A17 17 0 0 1 3 4a1 1 0 0 1 1-1h3.5a1 1 0 0 1 1 1c0 1.25.2 2.45.57 3.57a1 1 0 0 1-.25 1z"/></svg>
        1-888-555-0174
      </span>
      <span class="footer__item">
        <svg class="footer__icon" width="11" height="11" viewBox="0 0 24 24" aria-hidden="true"><circle cx="12" cy="12" r="10" fill="none" stroke="#fff" stroke-width="2.2"/><path d="M2 12h20M12 2c3 3 3 17 0 20M12 2c-3 3-3 17 0 20" fill="none" stroke="#fff" stroke-width="1.8"/></svg>
        www.resinora-coat.example
      </span>
    </div>
  </footer>
</section>

</body>
</html>
```